Quiet Harbour Counselling Flyer Design

I am a counsellor about to set up in independant practice. I need my flyer to tie in with my business card design. It should be simple / elegant on the outside face- dark blue background with white text. . The internal face could have a splash of colour to make it interesting. Perhaps an image of 'waves with the text over the top. With the quote underneath 'you can't stop the waves, but you can learn to surf'. Perhaps a border separating text info from quote. I want the text to be varying sizes and fonts so that it looks more interesting but still should feel simple. I have included the text I need, in the page order however I am open to suggestions about how this will look graphically. Please see business card design.i would like 'stars can't shine without darkness' to match business card.

I need it to look professional, elegant, simplistic but eye catching.

The logo was designed by inkmerrow

```html
<!DOCTYPE html>
<html lang="en">
<head>
<meta charset="utf-8">
<title>Quiet Harbour Counselling – Flyer</title>
<link href="https://fonts.googleapis.com/css2?family=EB+Garamond:ital,wght@0,400;0,600;1,400&family=Libre+Baskerville:wght@700&display=swap" rel="stylesheet">
<style>
  :root {
    --stage: #d9d9d9;
    --navy: #13234a;
    --navy-deep: #0a1430;
    --navy-mid: #1c3263;
    --ink: #0f1a36;
    --paper: #ffffff;
    --sky: #bfe0f5;
    --sky-soft: #e6f3fb;
    --rule: #9a9a9a;
    --photo-light: #dcdcdc;
    --photo-mid: #b9b6b3;
    --photo-dark: #3a3a3e;
  }
  * { box-sizing: border-box; margin: 0; padding: 0; }
  html, body {
    width: 1200px; height: 821px; overflow: hidden;
    background: var(--stage);
  }
  .flyer {
    position: absolute; left: 106px; top: 30px;
    width: 988px; height: 760px;
    display: flex;
    box-shadow: 0 6px 18px rgba(0,0,0,.25);
  }
  .panel { position: relative; height: 100%; overflow: hidden; }

  /* Left panel – contact */
  .panel--contact { width: 331px; background: var(--navy); }
  .contact__sheet {
    position: absolute; left: 9px; top: 9px; right: 9px; height: 590px;
    background: var(--paper);
  }
  .contact__flourish {
    position: absolute; left: 0; right: 0; top: 330px; height: 260px;
    background: linear-gradient(160deg, var(--paper) 10%, var(--sky-soft) 45%, var(--sky) 70%, var(--sky-soft) 100%);
  }
  .contact__curve { position: absolute; left: 0; top: 560px; width: 331px; height: 60px; }
  .contact__title {
    position: absolute; left: 36px; top: 100px;
    font: 700 29px/1 "Libre Baskerville", serif; color: var(--ink);
  }
  .contact__rule {
    position: absolute; left: 30px; top: 148px; width: 284px; height: 1px; background: var(--rule);
  }
  .contact__intro {
    position: absolute; left: 36px; top: 156px; width: 280px;
    font: 400 16px/20px "EB Garamond", serif; color: var(--ink);
  }
  .contact__phone {
    position: absolute; left: 36px; top: 268px;
    font: 400 35px/1 "EB Garamond", serif; color: var(--ink);
  }
  .contact__email {
    position: absolute; left: 36px; top: 311px;
    font: 400 14px/1 "EB Garamond", serif; color: var(--ink);
  }
  .contact__web {
    position: absolute; left: 36px; top: 516px; z-index: 2;
    font: 400 15px/1 "EB Garamond", serif; color: var(--ink);
  }
  .contact__motto {
    position: absolute; left: 36px; top: 652px;
    font: italic 400 21px/32px "EB Garamond", serif; color: var(--paper);
  }

  /* Middle panel – cover */
  .panel--cover {
    width: 328px;
    background: radial-gradient(ellipse at 50% 45%, var(--navy-mid) 0%, var(--navy) 55%, var(--navy-deep) 100%);
  }
  .cover__frame {
    position: absolute; inset: 8px; border: 1px solid rgba(255,255,255,.85);
  }
  .cover__name {
    position: absolute; left: 0; right: 0; top: 92px; text-align: center;
    font: italic 400 18px/1 "EB Garamond", serif; color: #c9cfdc;
  }
  .cover__stars { position: absolute; inset: 0; }
  .cover__tagline {
    position: absolute; left: 0; right: 0; top: 545px; text-align: center;
    font: 600 17px/1 "EB Garamond", serif; color: var(--paper);
  }

  /* Right panel – opener */
  .panel--opener { width: 329px; background: var(--photo-dark); }
  .opener__photo {
    position: absolute; inset: 0;
    background: linear-gradient(100deg, var(--photo-light) 0%, var(--photo-mid) 45%, var(--photo-dark) 80%);
  }
  .opener__title {
    position: absolute; left: 28px; top: 36px;
    font: 700 44px/46px "Libre Baskerville", serif; color: var(--ink);
  }
  .opener__strip {
    position: absolute;
    padding: 1px 9px 2px;
    background: var(--paper);
    box-shadow: 1px 2px 3px rgba(0,0,0,.3);
    font: 400 14px/1.1 "EB Garamond", serif; color: var(--ink);
    white-space: nowrap;
  }
  .opener__note {
    position: absolute; left: 28px; top: 474px; width: 290px;
    font: 400 15px/17.5px "EB Garamond", serif; color: var(--paper);
  }
  .opener__band {
    position: absolute; left: 0; right: 0; top: 582px; height: 92px;
    background: var(--paper);
    display: flex; align-items: center; justify-content: center;
  }
  .opener__band::after {
    content: ""; position: absolute; left: 0; right: 0; bottom: -8px; height: 3px; background: var(--paper);
  }
  .opener__name {
    font: 400 24px/1 "EB Garamond", serif; color: var(--ink);
  }
</style>
</head>
<body>
<svg width="0" height="0" style="position:absolute">
  <defs>
    <symbol id="star" viewBox="-1 -1 2 2">
      <polygon fill="#ffffff" points="0,-1 0.225,-0.309 0.951,-0.309 0.363,0.118 0.588,0.809 0,0.382 -0.588,0.809 -0.363,0.118 -0.951,-0.309 -0.225,-0.309"/>
    </symbol>
  </defs>
</svg>

<main class="flyer">
  <section class="panel panel--contact">
    <div class="contact__sheet">
      <div class="contact__flourish" role="img" aria-label="Soft pale blue floral swirl decoration"></div>
    </div>
    <svg class="contact__curve" viewBox="0 0 331 60" preserveAspectRatio="none">
      <path d="M0,22 Q160,-6 331,34 L331,60 L0,60 Z" fill="var(--navy)"/>
      <path d="M0,22 Q160,-6 331,34" fill="none" stroke="#ffffff" stroke-width="2"/>
    </svg>
    <h2 class="contact__title">Get in Touch</h2>
    <div class="contact__rule"></div>
    <p class="contact__intro">If you are curious about<br>how Quiet Harbour could help you<br>simply send me an email<br>or give me a call.</p>
    <p class="contact__phone">0700-914-2286</p>
    <p class="contact__email">hello@quietharbourcounselling.co.uk</p>
    <p class="contact__web">www.quietharbourcounselling.co.uk</p>
    <p class="contact__motto">By Changing Nothing,<br>Nothing Changes</p>
  </section>

  <section class="panel panel--cover">
    <div class="cover__frame"></div>
    <p class="cover__name">Quiet Harbour</p>
    <svg class="cover__stars" viewBox="0 0 328 760" aria-hidden="true">
      <use href="#star" x="52" y="196" width="7" height="7"/>
      <use href="#star" x="166" y="176" width="6" height="6"/>
      <use href="#star" x="146" y="248" width="5" height="5"/>
      <use href="#star" x="262" y="292" width="12" height="12"/>
      <use href="#star" x="96" y="328" width="14" height="14"/>
      <use href="#star" x="196" y="356" width="6" height="6"/>
      <use href="#star" x="40" y="468" width="5" height="5"/>
      <use href="#star" x="280" y="456" width="6" height="6"/>
      <use href="#star" x="144" y="612" width="7" height="7"/>
      <use href="#star" x="244" y="634" width="10" height="10"/>
      <use href="#star" x="84" y="686" width="6" height="6"/>
      <use href="#star" x="212" y="700" width="5" height="5"/>
    </svg>
    <p class="cover__tagline">Stars can’t shine without darkness</p>
  </section>

  <section class="panel panel--opener">
    <div class="opener__photo" role="img" aria-label="Photograph of a young woman sitting on the floor hugging her knees, looking downcast"></div>
    <h1 class="opener__title">Sound<br>familiar?</h1>
    <span class="opener__strip" style="left:32px;top:204px;transform:rotate(-1deg)">I’m struggling…</span>
    <span class="opener__strip" style="left:18px;top:238px;transform:rotate(1deg)">I’m feeling stressed…</span>
    <span class="opener__strip" style="left:55px;top:274px;transform:rotate(-1deg)">Life is overwhelming me…</span>
    <span class="opener__strip" style="left:18px;top:306px;transform:rotate(1deg)">I keep repeating the same mistakes…</span>
    <span class="opener__strip" style="left:41px;top:333px;transform:rotate(-1.5deg)">I’m unhappy…</span>
    <span class="opener__strip" style="left:24px;top:361px;transform:rotate(1.5deg)">I feel so alone…</span>
    <span class="opener__strip" style="left:41px;top:396px">I need someone to turn to…</span>
    <span class="opener__strip" style="left:18px;top:430px;transform:rotate(-0.5deg)">I want things to change…</span>
    <p class="opener__note">4 out of 5 of us will feel anxious,<br>stressed, depressed and stuck at<br>some point in life.<br>If this sounds like you<br>Quiet Harbour Counselling could help.</p>
    <div class="opener__band">
      <span class="opener__name">Quiet Harbour Counselling</span>
    </div>
  </section>
</main>
</body>
</html>
```